Accounting and Tax Professional

New business with a business model based on good service and bright staff,

Brin Kowalczyk B.Com CPA DIRECTOR

"Harbourline Ledger And Levy Pty Ltd"
ABN 47 583 016 728

Registered Tax Agent
PROFESSIONAL PERSONABLE TIMELY OR "PROFESSIONAL ADVICE TAILORED TO SUIT YOU"
Superannuation|Business services|Management consulting|Taxation|Software support
E Brin@HarbourlineLedgerAndLevy.example.au
WWW.HARBOURLINELEDGERANDLEVY.EXAMPLE.AU
Phone: +61 0438 715 906
24519 Corvell Ridge Road Marrowvale QLD 4352, Australia

hi, I have uploaded an .EPS logo as requested by one of the designers, let me know if this is not the right size for the business card. thanks Brin

Target Market(s)

Mainly Business clients

Industry/Entity Type

Business

Font styles to use
Serif

Colors
85acd3
3377b5

Requirements
Must have
• clean/crisp/well laid out

```html
<!DOCTYPE html>
<html lang="en">
<head>
<meta charset="utf-8">
<title>Harbourline Ledger And Levy – Business Card</title>
<link rel="stylesheet" href="https://fonts.googleapis.com/css2?family=Michroma&family=Questrial&display=swap">
<style>
  :root {
    --backdrop: #e4e4e4;
    --card: #ffffff;
    --ink: #2b2b2b;
    --muted: #8a8d91;
    --brand-blue: #7096bb;
    --brand-deep: #3377b5;
    --brand-light: #85acd3;
    --rule: #b9bcc0;
  }
  * { box-sizing: border-box; margin: 0; padding: 0; }
  html, body {
    width: 1200px; height: 900px; overflow: hidden;
    background: var(--backdrop);
  }
  .stage {
    width: 1200px; height: 900px;
    display: flex; align-items: center; justify-content: center;
  }
  .card {
    position: relative;
    width: 1000px; height: 571px;
    background: var(--card);
    box-shadow: 0 6px 24px rgba(0,0,0,0.12);
    overflow: hidden;
    font-family: "Michroma", sans-serif;
    color: var(--ink);
  }
  .card__swoosh {
    position: absolute; left: 0; top: 0;
    width: 1000px; height: 571px;
  }
  .brand {
    position: absolute; left: 150px; top: 95px;
    display: flex; align-items: center; gap: 22px;
  }
  .brand__dot {
    width: 78px; height: 78px; border-radius: 50%;
    background: var(--brand-blue);
    flex: none;
  }
  .brand__name {
    font-family: "Questrial", sans-serif;
    font-size: 36px; line-height: 1.12; font-weight: 400;
    letter-spacing: 2px; text-transform: uppercase;
    color: var(--ink);
  }
  .details {
    position: absolute; left: 70px; top: 245px;
    display: flex; align-items: stretch;
  }
  .person {
    width: 370px; padding-right: 26px;
    text-align: right;
  }
  .person__name {
    color: var(--brand-blue);
    font-size: 17px; letter-spacing: 1px;
    text-transform: uppercase;
  }
  .person__role {
    font-size: 12px; letter-spacing: 1px; margin-top: 8px;
    text-transform: uppercase;
  }
  .person__address {
    font-size: 12px; letter-spacing: 1px; line-height: 1.7;
    margin-top: 34px; text-transform: uppercase;
  }
  .divider {
    width: 1px; background: var(--rule);
  }
  .contact {
    list-style: none; padding-left: 24px;
  }
  .contact__item {
    display: flex; align-items: center; gap: 10px;
    font-size: 12px; letter-spacing: 0.5px; line-height: 1;
    height: 24px; white-space: nowrap;
  }
  .contact__item--gap { margin-top: 14px; }
  .contact__icon {
    width: 17px; height: 17px; flex: none;
  }
  .contact__email { font-size: 11px; }
</style>
</head>
<body>
<main class="stage">
  <article class="card">
    <svg class="card__swoosh" viewBox="0 0 1000 571" aria-hidden="true">
      <path d="M0,571 Q500,380 1000,571 Z" fill="var(--rule)"/>
      <path d="M0,571 Q500,392 1000,571 Z" fill="var(--card)"/>
      <path d="M0,571 Q500,400 1000,571 Z" fill="var(--brand-blue)"/>
    </svg>

    <header class="brand">
      <span class="brand__dot"></span>
      <h1 class="brand__name">Harbourline<br>Ledger And Levy Pty Ltd</h1>
    </header>

    <section class="details">
      <div class="person">
        <p class="person__name">Brin Kowalczyk</p>
        <p class="person__role">Owner / C.E.O</p>
        <p class="person__address">24519 Corvell Ridge Road,<br>Marrowvale QLD 4352</p>
      </div>
      <span class="divider"></span>
      <ul class="contact">
        <li class="contact__item">
          <svg class="contact__icon" viewBox="0 0 20 20" aria-hidden="true"><circle cx="10" cy="10" r="10" fill="var(--brand-blue)"/><path d="M7 5.5c.6 0 1.2 1.8 1.2 2.3S7.4 8.6 7.6 9.2c.5 1.2 1.7 2.5 3 3 .6.2 1-.8 1.5-.7s2.3.7 2.3 1.3c0 .8-1 1.7-1.8 1.7C8.9 14.5 5.5 11 5.5 7.3 5.5 6.4 6.3 5.5 7 5.5z" fill="#fff"/></svg>
          <span>+61 0438 715 906</span>
        </li>
        <li class="contact__item">
          <svg class="contact__icon" viewBox="0 0 20 20" aria-hidden="true"><circle cx="10" cy="10" r="10" fill="var(--brand-blue)"/><rect x="7" y="4.5" width="6" height="11" rx="1" fill="#fff"/><rect x="8" y="6" width="4" height="6.5" fill="var(--brand-blue)"/></svg>
          <span>+61 7 4630 2185</span>
        </li>
        <li class="contact__item">
          <svg class="contact__icon" viewBox="0 0 20 20" aria-hidden="true"><circle cx="10" cy="10" r="10" fill="var(--brand-blue)"/><rect x="5" y="8" width="10" height="6" rx="1" fill="#fff"/><rect x="7" y="5" width="6" height="3" fill="#fff"/></svg>
          <span>+61 7 4630 2186</span>
        </li>
        <li class="contact__item contact__item--gap">
          <svg class="contact__icon" viewBox="0 0 20 20" aria-hidden="true"><circle cx="10" cy="10" r="10" fill="var(--brand-blue)"/><rect x="5" y="6.5" width="10" height="7" fill="#fff"/><path d="M5 6.5l5 4 5-4" fill="none" stroke="var(--brand-blue)" stroke-width="1"/></svg>
          <span class="contact__email">Brin@HarbourlineLedgerAndLevy.example.au</span>
        </li>
        <li class="contact__item">
          <svg class="contact__icon" viewBox="0 0 20 20" aria-hidden="true"><circle cx="10" cy="10" r="10" fill="var(--brand-blue)"/><circle cx="10" cy="10" r="5" fill="none" stroke="#fff" stroke-width="1.2"/><ellipse cx="10" cy="10" rx="2" ry="5" fill="none" stroke="#fff" stroke-width="1"/><path d="M5 10h10" stroke="#fff" stroke-width="1"/></svg>
          <span class="contact__email">WWW.HARBOURLINELEDGERANDLEVY.EXAMPLE.AU</span>
        </li>
      </ul>
    </section>
  </article>
</main>
</body>
</html>
```